Need a weekly post illustration to show bands that play.
Example next week
Februaray
Fri 2nd 10pm Peter Malvey

Sat 3rd 3pm Front Bar Stonewicker
5;30pm Front Bar Gareth Pilby
8pm Front baR Colm Burke
8pm Outback DJ Sandy
10;30 stage Lanterns Westward
Sunday 4th 6;30pm Stonewicker
I have attached pictures of front of our venue and outback area.
Also sample posters from other venues and our own.
I have also attached past posters and all logos
Please email me if you require anything further
Example next week
Februaray
Fri 2nd 10pm Peter Malvey

8pm Front baR Colm Burke
8pm Outback DJ Sandy

Target Market(s)

every age group

Industry/Entity Type

pub

Font styles to use
Serif

Colors
FFC000
F8CF3A
FAE287
FDF2CF
FEFAEE
EB3D1F
EC4F4E
F09395
F8D3D4
FCEDEE

Requirements
Must have
• Specific band time , name of band and area of venue
Nice to have
• Our brand is red , black and gold of logo. Would like to see this
Should not have
• Inaccurate information. Correct times and bands

```html
<!DOCTYPE html>
<html lang="en">
<head>
<meta charset="utf-8">
<title>Keeffe's Bar – Saturday February 3rd</title>
<link rel="stylesheet" href="https://fonts.googleapis.com/css2?family=Oswald:wght@600;700&family=Cinzel:wght@700;800&display=swap">
<style>
  :root {
    --ink: #1a130d;
    --white: #ffffff;
    --gold: #ffc000;
    --gold-soft: #f8cf3a;
    --gold-pale: #fae287;
    --red: #eb3d1f;
    --brown: #a8743a;
    --line: #7a5530;
    --photo-edge: #efe2c4;
  }
  * { margin: 0; padding: 0; box-sizing: border-box; }
  html, body { width: 1200px; height: 1200px; overflow: hidden; background: #ffffff; }
  .poster {
    position: relative; width: 1200px; height: 1200px; overflow: hidden;
    font-family: "Cinzel", serif;
  }
  .venue-backdrop {
    position: absolute; inset: 0;
    background: linear-gradient(180deg, #1b1714 0%, #2a1a16 30%, #6d1616 45%, #c61d1d 60%, #a01818 80%, #8e8a86 92%, #b9b6b2 100%);
  }
  .scroll-art { position: absolute; inset: 0; }
  .headline {
    position: absolute; top: 50px; left: 0; width: 1200px; text-align: center;
    font-family: "Oswald", sans-serif; font-weight: 700; font-size: 50px;
    color: var(--white); letter-spacing: 0.5px; line-height: 1; white-space: nowrap;
  }
  .date-month, .date-day {
    position: absolute; left: 235px; width: 400px; text-align: right;
    font-family: "Oswald", sans-serif; font-weight: 700; font-size: 88px;
    line-height: 1; letter-spacing: 0.5px; white-space: nowrap;
  }
  .date-month { top: 144px; color: var(--white); text-shadow: 0 3px 6px rgba(0,0,0,.35); }
  .date-day { top: 231px; color: var(--ink); }
  .date-number {
    position: absolute; left: 670px; top: 151px; width: 287px; height: 170px;
    border: 6px solid var(--ink);
    background: linear-gradient(135deg, #7a5a1e 0%, var(--gold-soft) 35%, var(--gold-pale) 50%, var(--gold) 65%, #6b4c16 100%);
    display: flex; align-items: center; justify-content: center;
    font-family: "Oswald", sans-serif; font-weight: 700; font-size: 160px; line-height: 1;
    color: var(--ink);
  }
  .lineup { position: absolute; left: 204px; top: 0; width: 440px; }
  .act { position: absolute; left: 0; width: 440px; text-align: center; white-space: nowrap; }
  .act-name {
    display: inline-block; position: relative;
    font-weight: 700; font-size: 34px; color: var(--white); line-height: 1;
    text-transform: uppercase;
    padding: 0 6px 8px; border-bottom: 2px solid var(--line);
    text-shadow: 0 2px 3px rgba(0,0,0,.25);
  }
  .act-name::before {
    content: "★"; position: absolute; left: -40px; top: -4px;
    color: var(--brown); font-size: 36px; text-shadow: none;
  }
  .act-time {
    display: block; margin-top: 8px;
    font-weight: 700; font-size: 30px; color: var(--ink); line-height: 1;
  }
  .act-time small { font-size: 20px; }
  .column-rule { position: absolute; left: 625px; top: 366px; width: 2px; height: 414px; background: rgba(122,85,48,.6); }
  .headliner-banner {
    position: absolute; left: 167px; top: 811px; width: 524px; height: 86px;
    background: var(--white); white-space: nowrap;
    display: flex; align-items: center; justify-content: center; gap: 12px;
    font-weight: 700; font-size: 34px; color: var(--brown); line-height: 1;
  }
  .stage-photo {
    position: absolute; left: 62px; top: 900px; width: 714px; height: 320px;
    transform: rotate(1.5deg);
    border: 8px solid var(--photo-edge);
    background: radial-gradient(ellipse at 50% 20%, #3b5d86 0%, #1c2f4c 45%, #0b1220 100%);
  }
  .stage-time {
    position: absolute; left: 60px; top: 934px; width: 760px; text-align: center;
    font-family: "Cinzel", serif; font-weight: 700; font-size: 36px;
    color: var(--white); line-height: 1; white-space: nowrap;
  }
  .act-photo { position: absolute; border: 7px solid var(--photo-edge); box-shadow: 0 4px 10px rgba(0,0,0,.35); }
  .act-photo--duo { left: 708px; top: 340px; width: 362px; height: 240px; transform: rotate(2deg);
    background: linear-gradient(135deg, #6b4b3c 0%, #9c6a52 40%, #3e2a24 100%); }
  .act-photo--solo { left: 648px; top: 530px; width: 262px; height: 272px; transform: rotate(-2deg);
    background: linear-gradient(180deg, #b9c5b5 0%, #4a4c55 50%, #1a1d2a 100%); }
  .act-photo--singer { left: 870px; top: 578px; width: 266px; height: 290px; transform: rotate(5deg);
    background: linear-gradient(160deg, #2a2a3a 0%, #1a1820 60%, #3b2e2a 100%); }
  .act-photo--dj { left: 748px; top: 808px; width: 200px; height: 218px; transform: rotate(-2deg);
    background: linear-gradient(180deg, #e4e2de 0%, #c9c3bb 60%, #8a8580 100%); }
  .venue-mark {
    position: absolute; left: 893px; top: 910px; width: 260px; height: 260px;
    border-radius: 50%; background: #111;
    border: 8px solid #f4ecd8;
    display: flex; align-items: center; justify-content: center; text-align: center;
    font-weight: 800; font-size: 34px; line-height: 1.1; color: var(--gold);
  }
</style>
</head>
<body>
<main class="poster">
  <div class="venue-backdrop" role="img" aria-label="Photo of the pub's red shopfront at night"></div>

  <svg class="scroll-art" width="1200" height="1200" viewBox="0 0 1200 1200" aria-hidden="true">
    <defs>
      <linearGradient id="parchment" x1="0" y1="0" x2="1" y2="1">
        <stop offset="0" stop-color="#dcb782"/>
        <stop offset="0.5" stop-color="#c39661"/>
        <stop offset="1" stop-color="#ad7f48"/>
      </linearGradient>
      <linearGradient id="roll" x1="0" y1="0" x2="0" y2="1">
        <stop offset="0" stop-color="#b48752"/>
        <stop offset="0.35" stop-color="#f0d3a0"/>
        <stop offset="1" stop-color="#b78a55"/>
      </linearGradient>
    </defs>
    <path class="parchment-body" fill="url(#parchment)"
      d="M150 320 L1020 320 L1010 600 L1030 900 L1020 1200 L150 1200 L160 1120 L140 1000 L170 880 L150 760 L190 700 L150 620 L200 560 L160 470 L175 380 Z"/>
    <path class="parchment-roll" fill="url(#roll)"
      d="M110 150 L150 160 L170 124 L1060 128 L1090 150 L1070 175 L1095 200 L1078 240 L1100 270 L1080 300 L1090 336 L170 336 L132 320 L150 290 L100 270 L130 240 L98 215 L130 190 Z"/>
  </svg>

  <h1 class="headline">★★★ KEEFFE'S BAR PRESENT ★★★</h1>

  <div class="date-month">FEBRUARY</div>
  <div class="date-day">SATURDAY</div>
  <div class="date-number">3RD</div>

  <section class="lineup">
    <div class="act" style="top:362px"><span class="act-name">Stonewicker</span><span class="act-time">3PM- <small>FRONT BAR</small></span></div>
    <div class="act" style="top:474px"><span class="act-name">Gareth Pilby</span><span class="act-time">5:30 PM- <small>FRONT BAR</small></span></div>
    <div class="act" style="top:590px"><span class="act-name">Colm Burke</span><span class="act-time">8PM- <small>FRONT BAR</small></span></div>
    <div class="act" style="top:696px"><span class="act-name">DJ Sandy</span><span class="act-time">8PM- <small>OUTBACK</small></span></div>
  </section>
  <div class="column-rule"></div>

  <div class="act-photo act-photo--duo" role="img" aria-label="Photo of Stonewicker performing in the front bar"></div>
  <div class="act-photo act-photo--solo" role="img" aria-label="Photo of Gareth Pilby singing with guitar"></div>
  <div class="act-photo act-photo--singer" role="img" aria-label="Photo of Colm Burke singing at the microphone"></div>
  <div class="act-photo act-photo--dj" role="img" aria-label="Portrait photo of DJ Sandy"></div>

  <div class="stage-photo" role="img" aria-label="Photo of Lanterns Westward playing on a lit stage"></div>
  <div class="stage-time">10:30PM- STAGE</div>
  <div class="headliner-banner"><span>★</span><span>LANTERNS WESTWARD</span></div>

  <div class="venue-mark">KEEFFE'S<br>BAR</div>
</main>
</body>
</html>
```